Building and Facilities Management brochure

Please refer to attached PDF, page by page with information about the brief.
SOPHISTICATED, BOLD, PROFESSIONAL BROCHURE to market our company in business meetings to Builders, Owners of buildings, Strata Committees etc.

The final design should portray quality, service, integrity,
Clear Communication

Attached is:
- pdf with details of basic layout options and wording and most of the information about the brief.
- Logo options to use
- Business card designs to understand what design we have previously had.
- Word document of the pdf if that helps to copy the information.

Target Market(s)

Professionals. Builders/developer, Strata Owners, and Building owners who want a high level of service and management of their building

Industry/Entity Type

It Company

Requirements
Must have
• - Logo
• - Contact details
• - Use of the colour in the design which has been specified.
• - Images/s of building/s
• - Use the phrase "Quality Service with Integrity"
Nice to have
• - as much of the wording as possible from the document which was uploaded, that will fit and work with the design
Should not have
• Excessive colour or variances as it needs to stay clear, bold and sophisticated.
• Too much on the page, clarity is key for clear communication without trying to clutter too much on the page.

```html
<!DOCTYPE html>
<html lang="en">
<head>
<meta charset="utf-8">
<title>NVS Brochure Spread</title>
<link href="https://fonts.googleapis.com/css2?family=Didact+Gothic&display=swap" rel="stylesheet">
<style>
  :root {
    --slate: #3d4550;
    --band-grey: #a3a5ad;
    --ink: #3a3d42;
    --accent: #2aa8df;
    --paper: #f7f8f9;
    --white: #ffffff;
  }
  * { margin: 0; padding: 0; box-sizing: border-box; }
  html, body { width: 1200px; height: 851px; overflow: hidden; background: var(--white); }
  .spread {
    position: relative; width: 1200px; height: 851px; overflow: hidden;
    font-family: "Didact Gothic", sans-serif; color: var(--ink);
  }
  .skyline-backdrop {
    position: absolute; inset: 0;
    background: linear-gradient(180deg, #eef0f2 0%, #f4f5f6 40%, #f9fafa 70%, #ffffff 100%);
  }
  .curves { position: absolute; inset: 0; width: 1200px; height: 851px; }
  .brand {
    position: absolute; top: 24px; left: 1092px;
    font-size: 28px; color: var(--accent); letter-spacing: 1px;
  }
  .intro {
    position: absolute; left: 118px; top: 204px; width: 374px;
    font-size: 11.6px; line-height: 19.2px; text-align: justify;
  }
  .intro p + p { margin-top: 8px; }
  .intro .lead { font-size: 17px; }
  .aspects {
    position: absolute; left: 709px; top: 208px; width: 370px;
    font-size: 11.2px; line-height: 13px; text-align: justify;
  }
  .aspects h2 { font-size: 11.6px; font-weight: normal; margin-bottom: 5px; }
  .aspects p + p { margin-top: 8px; }
  .aspects .term { color: var(--accent); }
  .services {
    position: absolute; top: 824px; font-size: 15.5px; letter-spacing: 2px;
    color: var(--white); text-transform: uppercase; white-space: nowrap;
  }
  .services.left { left: 94px; }
  .services.right { left: 709px; }
  .services .dot { margin: 0 10px; }
</style>
</head>
<body>
<main class="spread">
  <div class="skyline-backdrop" role="img" aria-label="Faint city skyline photograph washed out behind the text"></div>

  <svg class="curves" viewBox="0 0 1200 851" aria-hidden="false">
    <defs>
      <linearGradient id="cityTones" x1="0" y1="0" x2="0" y2="1">
        <stop offset="0" stop-color="#c9ced4"/>
        <stop offset="0.35" stop-color="#9aa2ab"/>
        <stop offset="0.6" stop-color="#4d5660"/>
        <stop offset="0.8" stop-color="#3f5a35"/>
        <stop offset="1" stop-color="#4f6f3c"/>
      </linearGradient>
    </defs>
    <path d="M0,0 H1200 V128 Q600,-46 0,124 Z" fill="var(--band-grey)"/>
    <path d="M0,0 H1200 V120 Q600,-54 0,116 Z" fill="var(--slate)"/>
    <path d="M0,616 Q600,408 1200,612 V851 H0 Z" fill="var(--band-grey)"/>
    <path d="M0,626 Q600,420 1200,622 V851 H0 Z" fill="url(#cityTones)" role="img" aria-label="City skyline photograph with towers, cloudy sky and green parkland"/>
  </svg>

  <div class="brand">NVS</div>

  <section class="intro">
    <p><span class="lead">At NVS,</span> our aim is to provide complete solutions for Building and Facilities Owners and Strata Corporations in the management of their assets. With the understanding that each property has different needs and requirements, our focus is to work with clients to tailor solutions best suited to their specific needs.</p>
    <p>Our aim is to ensure the Building and Facilities are managed to the highest standards using the latest technological management solutions to efficiently and effectively control all aspects of the building. With a keen focus on controlling costs to ensure funds are spent cost- effectively, through improved operations and management of all aspects of the building.</p>
  </section>

  <section class="aspects">
    <h2>Key Aspects:</h2>
    <p><span class="term">Compliance</span> - with relevant industry acts and regulations OH&amp;S - to ensure the building and aspects are controlled safely and the risk of all contractors and owners is reduced and managed.</p>
    <p><span class="term">Preventative Maintenance</span> - to ensure assets are professionally maintained to ensure the best reliability and longevity of each asset. Reactive Maintenance - to ensure any issues that arise are resolved and handled as efficiently as possible.</p>
    <p><span class="term">Communication</span> - to ensure the Committee and Owners have clear and concise information and knowledge of the aspects of their building and assets</p>
    <p><span class="term">Relationships</span> - are a top priority as they are paramount for effective management with Owners, Residents, Developers and Strata Managers</p>
  </section>

  <div class="services left">Core Services<span class="dot">•</span>Building Management</div>
  <div class="services right">Facilities Management<span class="dot">•</span>Caretaker</div>
</main>
</body>
</html>
```